Web Page Design for a Website that Provides Tutoring

I am looking to create an online tutoring website. The website will allow parents or students to contact tutors with a view to instructing them to tutor themselves or their children.

The name of the website is LendYourLessons.

This brief is to create the design for one of the web pages for this web site. I am hoping the same designer will be available to design other pages.

The page I want designed is one of the more complex and I have attached the design as an excel spreadsheet. The web page needs to include all the items on this page but if you want to change the positioning of the items then Im fine with that.

I recently had two logos created for this website. My favourite is the one with a mortar board but im not sure I like the colours. I have attached both of these logos and you can use either of them, change the colours or create something different. I just want a design pleasing to the eye. If the logo is changed I would like that in a seperate file.

So can you please submit designs for this page. I have attached the two logos which you can use, change or if you feel you have a better idea then you can use that.

On the spreadsheet the Send Message, Favourite etc are buttons.

Target Market(s)

People who want to better themselves.
Possible middle class to upper class.

Industry/Entity Type

Tutoring

Number of Pages Required

1 page

Requirements
Must have
• The designs must have alot of the information attached in the spreadsheet.

```html
<!DOCTYPE html>
<html lang="en">
<head>
<meta charset="utf-8">
<title>LendYourLessons – Tutor Profile</title>
<link href="https://fonts.googleapis.com/css2?family=Open+Sans:ital,wght@0,400;0,600;0,700;1,400&display=swap" rel="stylesheet">
<style>
:root{
  --coral:#f47a5b;
  --coral-soft:#f6a58f;
  --ink:#333333;
  --grey:#777777;
  --line:#d9d6d1;
  --sand:#f0ede8;
  --sand-dark:#d8d2c6;
  --white:#ffffff;
  --olive:#9d9b33;
  --amber:#ffa800;
  --sky:#1ea6dc;
  --star-grey:#cfcfcf;
  --video:#3a3a36;
}
*{margin:0;padding:0;box-sizing:border-box}
html,body{width:1200px;height:2594px;overflow:hidden}
body{font-family:"Open Sans",Arial,sans-serif;color:var(--ink);background:var(--sand);position:relative}
.abs{position:absolute}
section{position:absolute;left:0;width:1200px}

/* header */
.site-header{top:0;height:220px;background:var(--sand)}
.brand{left:0;width:1200px;top:48px;text-align:center;font-size:44px;font-weight:600;color:var(--coral);letter-spacing:-1px}
.nav a{position:absolute;top:146px;transform:translateX(-50%);font-size:13px;letter-spacing:1px;color:#6a6a6a;text-decoration:none;text-transform:uppercase}
.nav a.active{color:var(--coral);font-weight:600}
.nav a.active::after{content:"";position:absolute;left:-4px;right:-4px;bottom:-7px;height:2px;background:var(--coral)}

/* profile */
.profile{top:220px;height:553px;background:var(--white)}
.photo{left:95px;top:51px;width:197px;height:191px;border:1px solid #cfcfcf;padding:3px;background:var(--white);box-shadow:0 2px 3px rgba(0,0,0,.15)}
.photo div{width:100%;height:100%;background:linear-gradient(180deg,#d8d5d0 0%,#a67f66 45%,#e6e1db 100%)}
.tutor-name{left:329px;top:47px;font-size:28px;font-weight:700;color:var(--ink)}
.tutor-name span{color:var(--coral)}
.activity{left:473px;top:62px;font-size:11px;font-style:italic;color:#999}
.icon-btn{top:52px;width:31px;height:27px;background:var(--coral);border-radius:4px;display:flex;align-items:center;justify-content:center}
.profile-rule{left:329px;top:113px;width:778px;height:1px;background:var(--line)}
.rating{top:140px;width:200px;transform:translateX(-50%);text-align:center}
.rating h3{font-size:17px;font-weight:400;color:var(--ink)}
.rating svg{display:block;margin:10px auto 0}
.rating .score{font-size:20px;font-weight:700;margin-top:4px}
.facts{left:95px;top:288px}
.fact{display:flex;align-items:center;height:35px;font-size:11px;font-weight:700;letter-spacing:.5px;text-transform:uppercase;color:var(--ink)}
.tag{margin-left:8px;background:var(--coral);color:var(--white);font-weight:400;font-size:10.5px;padding:1px 6px;border-radius:2px}
.cert-badge{left:95px;top:432px;width:71px;height:52px;border:2px solid var(--coral);background:#fff6f3}
.bio{left:399px;top:281px;width:708px;font-size:14px;line-height:35px;color:#666;text-align:justify}

/* headings */
.section-title{font-size:29px;font-weight:700;color:var(--ink)}
.section-title span{color:var(--coral);font-weight:600}
.rule{height:1px;background:var(--line)}

/* subjects */
.subjects{top:773px;height:481px;background:var(--sand)}
.price-table{left:107px;top:152px;width:986px;border-collapse:separate;border-spacing:0;background:var(--white)}
.price-table th{height:45px;background:var(--coral);color:var(--white);font-size:15px;font-weight:600;border-left:3px solid var(--sand)}
.price-table th:first-child{border-left:none}
.price-table td{border-left:3px solid #ececec;text-align:center;font-size:15px;color:var(--ink)}
.price-table td:first-child{border-left:none}
.subject-badge{display:inline-flex;align-items:center;gap:8px;width:157px;height:41px;padding-left:14px;border-radius:3px;color:var(--white);font-size:15px;font-weight:700;text-transform:uppercase}
.chem{background:var(--amber)}
.bio-b{background:var(--olive)}

/* schedule */
.schedule{top:1254px;height:703px;background:var(--white)}
.month{left:250px;top:130px;width:220px;display:flex;align-items:center;justify-content:space-between;color:var(--coral);font-size:23px;font-weight:600;letter-spacing:2px}
.weekdays{left:107px;top:183px;width:503px;display:grid;grid-template-columns:repeat(7,1fr);text-align:center;font-size:16px}
.calendar{left:107px;top:1477px;top:223px;width:503px;border-top:5px solid var(--coral);display:grid;grid-template-columns:repeat(7,1fr);background:#e6e3de;gap:1px}
.day{height:71px;background:var(--sand);font-size:14px;color:var(--coral);padding:6px 0 0 8px}
.day.taken{background:var(--coral);color:var(--white)}
.day.reserved{background:var(--amber);color:var(--white)}
.day.holiday{background:var(--olive);color:var(--white)}
.day.off{background:var(--sky);color:var(--white)}
.legend{left:107px;top:624px;display:flex;gap:26px;font-size:13px;text-transform:uppercase}
.legend span::before{content:"";display:inline-block;width:10px;height:10px;margin-right:9px;background:var(--c)}
.btn{left:718px;width:280px;height:54px;display:flex;align-items:center;justify-content:center;font-size:16px;border-radius:2px}
.btn-solid{top:297px;background:var(--coral);color:var(--white)}
.btn-outline{top:439px;border:1.5px solid var(--coral);color:var(--coral);background:var(--white)}
.or{left:718px;width:280px;top:382px;text-align:center;color:#999;font-size:16px}

/* reviews */
.reviews{top:1957px;height:616px;background:var(--sand)}
.reviews .section-title{left:78px;top:28px}
.review-summary{left:78px;top:116px;font-size:13px;font-style:italic;color:#777}
.review{left:102px;width:398px;height:168px;background:var(--white);border-radius:3px;box-shadow:0 1px 4px rgba(0,0,0,.15)}
.review::after{content:"";position:absolute;left:52px;bottom:-18px;border-left:0 solid transparent;border-right:22px solid transparent;border-top:18px solid var(--white)}
.avatar{left:12px;top:16px;width:58px;height:44px;background:#f8c9bc;border-radius:4px}
.reviewer{left:85px;top:20px;font-size:17px;font-weight:700;display:flex;align-items:center;gap:10px}
.reviewer span{color:var(--coral)}
.review p{left:85px;top:58px;width:296px;font-size:13px;line-height:19px;color:#666}
.review time{right:16px;top:138px;font-size:15px;color:#999}
.video{left:610px;top:152px;width:542px;height:338px;border:10px solid #bdbcb9;background:var(--video)}
.video-brand{right:20px;top:252px;font-size:18px;font-weight:600;color:var(--white);letter-spacing:-.5px}
.video-bar{left:16px;right:16px;top:285px;height:2px;background:#bbb}
.footer-band{top:2573px;height:21px;background:var(--sand-dark)}
</style>
</head>
<body>
<svg width="0" height="0" style="position:absolute">
  <defs>
    <symbol id="star" viewBox="0 0 20 20"><path d="M10 1l2.7 5.6 6.1.9-4.4 4.3 1 6.1L10 15l-5.4 2.9 1-6.1L1.2 7.5l6.1-.9z"/></symbol>
    <clipPath id="half"><rect x="0" y="0" width="10" height="20"/></clipPath>
  </defs>
</svg>

<header class="site-header abs">
  <div class="brand abs">LendYourLessons</div>
  <nav class="nav">
    <a href="#" style="left:259px">Home</a>
    <a href="#" style="left:346px">Search</a>
    <a href="#" style="left:444px">Student</a>
    <a href="#" class="active" style="left:541px">Tutor</a>
    <a href="#" style="left:633px">About</a>
    <a href="#" style="left:730px">Contact</a>
    <a href="#" style="left:832px">Sign In</a>
    <a href="#" style="left:930px">Register</a>
  </nav>
</header>

<section class="profile">
  <div class="photo abs"><div role="img" aria-label="Portrait photo of the tutor"></div></div>
  <h1 class="tutor-name abs"><span>Jane</span> Doe</h1>
  <div class="activity abs">active 15 minutes ago</div>
  <a class="icon-btn abs" style="left:950px" aria-label="Send message"><svg width="17" height="12" viewBox="0 0 17 12"><rect x=".5" y=".5" width="16" height="11" fill="none" stroke="#fff"/><path d="M.5 .5l8 6 8-6" fill="none" stroke="#fff"/></svg></a>
  <a class="icon-btn abs" style="left:1012px" aria-label="Favourite"><svg width="16" height="16" fill="#fff"><use href="#star"/></svg></a>
  <a class="icon-btn abs" style="left:1073px" aria-label="Chat"><svg width="18" height="15" viewBox="0 0 18 15"><path d="M9 1C4.6 1 1 3.6 1 6.7c0 1.7 1 3.2 2.7 4.2L3 14l3.6-2c.8.2 1.6.3 2.4.3 4.4 0 8-2.6 8-5.6S13.4 1 9 1z" fill="#fff"/></svg></a>
  <div class="profile-rule abs"></div>

  <div class="rating abs" style="left:491px">
    <h3>Review Score</h3>
    <svg width="112" height="20" fill="#f7941d">
      <use href="#star" x="0" width="20" height="20"/><use href="#star" x="23" width="20" height="20"/><use href="#star" x="46" width="20" height="20"/><use href="#star" x="69" width="20" height="20"/>
      <use href="#star" x="92" width="20" height="20" fill="var(--star-grey)"/>
      <g transform="translate(92 0)"><use href="#star" width="20" height="20" clip-path="url(#half)"/></g>
    </svg>
    <div class="score" style="color:#f7941d">4.5/5</div>
  </div>
  <div class="rating abs" style="left:714px">
    <h3>Reliability</h3>
    <svg width="112" height="20" fill="var(--olive)">
      <use href="#star" x="0" width="20" height="20"/><use href="#star" x="23" width="20" height="20"/><use href="#star" x="46" width="20" height="20"/><use href="#star" x="69" width="20" height="20"/>
      <use href="#star" x="92" width="20" height="20" fill="var(--star-grey)"/>
    </svg>
    <div class="score" style="color:var(--olive)">4.0/5</div>
  </div>
  <div class="rating abs" style="left:928px">
    <h3>Punctuality</h3>
    <svg width="112" height="20" fill="var(--sky)">
      <use href="#star" x="0" width="20" height="20"/><use href="#star" x="23" width="20" height="20"/><use href="#star" x="46" width="20" height="20"/><use href="#star" x="69" width="20" height="20"/>
      <use href="#star" x="92" width="20" height="20" fill="var(--star-grey)"/>
      <g transform="translate(92 0)"><use href="#star" width="20" height="20" clip-path="url(#half)"/></g>
    </svg>
    <div class="score" style="color:var(--sky)">4.6/5</div>
  </div>

  <div class="facts abs">
    <div class="fact">Tutoring type: <span class="tag">Personal</span></div>
    <div class="fact">Willing to travel: <span class="tag">Home only</span></div>
    <div class="fact">Age: <span class="tag">20 years old</span></div>
    <div class="fact">Member since: <span class="tag">December 2013</span></div>
  </div>
  <div class="cert-badge abs" role="img" aria-label="Background check badge"></div>

  <p class="bio abs">Lorem ipsum dolor sit amet, consectetur adipiscing elit, sed do eiusmod tempor incididunt ut labore et dolore magna aliqua. Ut enim ad minim veniam, quis nostrud exercitation ullamco laboris nisi ut aliquip ex ea commodo consequat. Duis aute irure dolor in reprehenderit in voluptate velit esse cillum dolore eu fugiat nulla pariatur. Excepteur sint occaecat cupidatat non proident, sunt in culpa qui officia deserunt mollit anim id est laborum.Ut enim ad minim veniam, quis nostrud exercitation ullamco laboris nisi ut aliquip ex ea commodo consequat. Duis aute irure dolor in reprehenderit in voluptate velit esse cillum dolore eu fugiat nulla pariatur.</p>
</section>

<section class="subjects">
  <h2 class="section-title abs" style="left:107px;top:44px"><span>Subjects</span> Taught</h2>
  <div class="rule abs" style="left:107px;top:109px;width:987px"></div>
  <table class="price-table abs">
    <colgroup><col style="width:165px"><col style="width:137px"><col style="width:137px"><col style="width:137px"><col style="width:137px"><col style="width:137px"><col style="width:136px"></colgroup>
    <thead><tr><th>Subjects</th><th>Primary</th><th>Secondary</th><th>GCSE</th><th>A- Level</th><th>University</th><th>Adult Learing</th></tr></thead>
    <tbody>
      <tr style="height:44px"><td></td><td></td><td></td><td></td><td></td><td></td><td></td></tr>
      <tr style="height:41px">
        <td><span class="subject-badge chem"><svg width="14" height="18" viewBox="0 0 14 18"><path d="M5 1h4M5.5 1v6L1 16h12L8.5 7V1" fill="none" stroke="#fff" stroke-width="1.5"/></svg>Chemistry</span></td>
        <td>£20</td><td></td><td>£25</td><td>£30</td><td></td><td></td>
      </tr>
      <tr style="height:21px"><td></td><td></td><td></td><td></td><td></td><td></td><td></td></tr>
      <tr style="height:41px">
        <td><span class="subject-badge bio-b"><svg width="14" height="18" viewBox="0 0 14 18"><path d="M6 1l3 2-3 6-3-2zM4 12a5 5 0 0 0 8-4M1 17h12M7 13v4" fill="none" stroke="#fff" stroke-width="1.5"/></svg>Biology</span></td>
        <td>£20</td><td></td><td>£25</td><td>£30</td><td></td><td></td>
      </tr>
      <tr style="height:52px"><td></td><td></td><td></td><td></td><td></td><td></td><td></td></tr>
    </tbody>
  </table>
</section>

<section class="schedule">
  <h2 class="section-title abs" style="left:107px;top:35px"><span>Available</span> Schedule</h2>
  <div class="rule abs" style="left:107px;top:103px;width:917px"></div>
  <div class="month abs">
    <svg width="10" height="12"><path d="M9 1L1 6l8 5z" fill="var(--coral)"/></svg>
    DECEMBER
    <svg width="10" height="12"><path d="M1 1l8 5-8 5z" fill="var(--coral)"/></svg>
  </div>
  <div class="weekdays abs"><span>Su</span><span>Mo</span><span>Tu</span><span>We</span><span>Th</span><span>Fr</span><span>Sa</span></div>
  <div class="calendar abs">
    <div class="day"></div><div class="day"></div><div class="day"></div><div class="day"></div>
    <div class="day">1</div><div class="day">2</div><div class="day taken">3</div>
    <div class="day off">4</div><div class="day">5</div><div class="day">6</div><div class="day">7</div><div class="day taken">8</div><div class="day">9</div><div class="day">10</div>
    <div class="day">11</div><div class="day">12</div><div class="day taken">13</div><div class="day">14</div><div class="day">15</div><div class="day">16</div><div class="day reserved">17</div>
    <div class="day">18</div><div class="day">19</div><div class="day">20</div><div class="day">21</div><div class="day">22</div><div class="day taken">23</div><div class="day">24</div>
    <div class="day holiday">25</div><div class="day">26</div><div class="day">27</div><div class="day">28</div><div class="day">29</div><div class="day">30</div><div class="day holiday">31</div>
  </div>
  <div class="legend abs">
    <span style="--c:var(--coral)">Taken</span>
    <span style="--c:var(--amber)">Reserved</span>
    <span style="--c:var(--olive)">Holiday</span>
    <span style="--c:var(--sky)">Not available</span>
  </div>
  <a class="btn btn-solid abs">Set an Appointment</a>
  <div class="or abs">or</div>
  <a class="btn btn-outline abs">Reserve a Date</a>
</section>

<section class="reviews">
  <h2 class="section-title abs">Reviews</h2>
  <a class="icon-btn abs" style="left:491px;top:34px" aria-label="Write a review"><svg width="18" height="15" viewBox="0 0 18 15"><path d="M9 1C4.6 1 1 3.6 1 6.7c0 1.7 1 3.2 2.7 4.2L3 14l3.6-2c.8.2 1.6.3 2.4.3 4.4 0 8-2.6 8-5.6S13.4 1 9 1z" fill="#fff"/></svg></a>
  <div class="rule abs" style="left:78px;top:97px;width:448px"></div>
  <div class="review-summary abs">2 reviews with an average rating of 4.0</div>

  <article class="review abs" style="top:166px">
    <div class="avatar abs" role="img" aria-label="Reviewer icon"></div>
    <div class="reviewer abs"><div><span>John</span> Doe</div>
      <svg width="104" height="18" fill="#f7941d"><use href="#star" x="0" width="18" height="18"/><use href="#star" x="21" width="18" height="18"/><use href="#star" x="42" width="18" height="18"/><use href="#star" x="63" width="18" height="18"/><use href="#star" x="84" width="18" height="18" fill="var(--star-grey)"/></svg>
    </div>
    <p class="abs">Lorem ipsum dolor sit amet, consectetur adipiscing elit, sed do eiusmod tempor incididunt ut labore et dolore magna aliqua.</p>
    <time class="abs">3 days ago</time>
  </article>

  <article class="review abs" style="top:375px">
    <div class="avatar abs" role="img" aria-label="Reviewer icon"></div>
    <div class="reviewer abs"><div><span>Jane</span> Doe</div>
      <svg width="104" height="18" fill="#f7941d"><use href="#star" x="0" width="18" height="18"/><use href="#star" x="21" width="18" height="18"/><use href="#star" x="42" width="18" height="18"/><use href="#star" x="63" width="18" height="18"/><use href="#star" x="84" width="18" height="18" fill="var(--star-grey)"/></svg>
    </div>
    <p class="abs">Lorem ipsum dolor sit amet, consectetur adipiscing elit, sed do eiusmod tempor incididunt ut labore et dolore magna aliqua.</p>
    <time class="abs">3 days ago</time>
  </article>

  <div class="video abs" role="img" aria-label="Tutor introduction video player">
    <div class="video-brand abs">LendYourLessons</div>
    <div class="video-bar abs"></div>
    <svg class="abs" style="left:16px;top:296px" width="12" height="12"><path d="M2 1l9 5-9 5z" fill="#fff"/></svg>
    <svg class="abs" style="right:40px;top:298px" width="12" height="9"><rect width="12" height="9" rx="1" fill="#ddd"/></svg>
    <svg class="abs" style="right:18px;top:297px" width="11" height="11"><path d="M1 4V1h3M7 1h3v3M10 7v3H7M4 10H1V7" fill="none" stroke="#ddd" stroke-width="1.4"/></svg>
  </div>
</section>

<div class="footer-band abs" style="left:0;width:1200px"></div>
</body>
</html>
```